Upscale business cards needed for Board of Directors

We need professional business cards created for members of our family business Board of Directors. We would like these relatively simple and straightforward, but also with a unique element to set them apart. Probably stick with neutral and simple colors - white, grey etc. We need space for the traditional elements, including name, title, address, email/phone number. And we will be creating several from this template so it needs to be template that is easy to switch information in and out of.
Business
See description

```html
<!DOCTYPE html>
<html lang="en">
<head>
<meta charset="utf-8">
<title>Harbourline Holdings – Business Card</title>
<link rel="stylesheet" href="https://fonts.googleapis.com/css2?family=Roboto:wght@300;400;700&display=swap">
<style>
  :root {
    --backdrop: #ecebe6;
    --card-white: #ffffff;
    --card-shade: #f1f1ef;
    --gold: #b8aa7e;
    --tan-light: #cbc198;
    --tan-dark: #a69a70;
    --ink: #1f1f1f;
    --ink-soft: #3a3a3a;
  }
  * { margin: 0; padding: 0; box-sizing: border-box; }
  html, body { width: 1200px; height: 1023px; overflow: hidden; }
  body {
    background: var(--backdrop);
    font-family: "Roboto", Arial, sans-serif;
    display: flex;
    flex-direction: column;
    align-items: center;
    justify-content: center;
    gap: 80px;
  }
  .card {
    position: relative;
    width: 620px;
    height: 354px;
    border-radius: 14px;
    overflow: hidden;
    box-shadow: 0 4px 14px rgba(0,0,0,0.12);
  }
  .card--front {
    background: radial-gradient(circle at 55% 45%, var(--card-white) 0%, var(--card-white) 45%, var(--card-shade) 100%);
  }
  .card--back {
    background: linear-gradient(160deg, var(--tan-light) 0%, #c2b78d 45%, var(--tan-dark) 100%);
  }
  .edge-line {
    position: absolute;
    left: 26px;
    top: 0;
    width: 6px;
    height: 248px;
    background: var(--gold);
  }
  .edge-bar {
    position: absolute;
    right: 22px;
    bottom: 0;
    width: 9px;
    height: 92px;
    background: var(--gold);
  }
  .company-name {
    position: absolute;
    font-weight: 700;
    line-height: 1;
    text-transform: uppercase;
  }
  .card--front .company-name {
    right: 58px;
    top: 42px;
    text-align: right;
    color: var(--ink);
  }
  .company-name .word-main { display: block; font-size: 40px; letter-spacing: 0.5px; }
  .company-name .word-sub { display: block; font-size: 18px; letter-spacing: 10px; margin-top: 6px; margin-right: -10px; }
  .card--back .company-name {
    left: 0; right: 0;
    top: 50%;
    transform: translateY(-50%);
    text-align: center;
    color: var(--card-white);
  }
  .card--back .company-name .word-main { font-size: 48px; }
  .card--back .company-name .word-sub { font-size: 22px; letter-spacing: 12px; margin-right: -12px; }
  .person {
    position: absolute;
    left: 58px;
    top: 88px;
  }
  .person-name { font-size: 26px; font-weight: 400; color: var(--ink); letter-spacing: 0.3px; }
  .person-title { font-size: 14px; font-weight: 300; color: var(--gold); margin-top: 2px; }
  .contacts {
    position: absolute;
    left: 58px;
    top: 262px;
    list-style: none;
    font-size: 12.5px;
    font-weight: 400;
    color: var(--ink-soft);
    letter-spacing: 0.4px;
  }
  .contacts li { display: flex; align-items: flex-start; gap: 10px; line-height: 17px; }
  .contacts svg { width: 11px; height: 11px; margin-top: 3px; flex: none; }
  .website {
    position: absolute;
    right: 48px;
    bottom: 22px;
    font-size: 12.5px;
    letter-spacing: 0.8px;
    color: var(--ink-soft);
  }
  .website .accent { color: var(--gold); }
</style>
</head>
<body>

<section class="card card--front" aria-label="Business card front">
  <div class="edge-line"></div>
  <div class="edge-bar"></div>

  <h1 class="company-name">
    <span class="word-main">Harbourline</span>
    <span class="word-sub">Holdings</span>
  </h1>

  <div class="person">
    <p class="person-name">Your Name</p>
    <p class="person-title">Title</p>
  </div>

  <ul class="contacts">
    <li>
      <svg viewBox="0 0 12 12" aria-hidden="true"><circle cx="6" cy="6" r="5.2" fill="none" stroke="var(--gold)" stroke-width="1"/><path d="M4.3 3.4c.4-.3.8 0 1 .5l.2.6c.1.3 0 .5-.3.7.3.7.8 1.2 1.5 1.5.2-.3.4-.4.7-.3l.6.2c.5.2.8.6.5 1-.6.8-1.6.7-2.7-.1-1-.8-1.8-1.9-1.8-2.9 0-.5.1-.9.3-1.2z" fill="var(--gold)"/></svg>
      <span>88-123-54321</span>
    </li>
    <li>
      <svg viewBox="0 0 12 12" aria-hidden="true"><rect x="1" y="2.5" width="10" height="7" fill="none" stroke="var(--gold)" stroke-width="1"/><path d="M1 2.5l5 4 5-4" fill="none" stroke="var(--gold)" stroke-width="1"/></svg>
      <span>info@yourweb.com</span>
    </li>
    <li>
      <svg viewBox="0 0 12 12" aria-hidden="true"><path d="M6 11.5C4 8.8 2.6 7 2.6 4.9a3.4 3.4 0 0 1 6.8 0C9.4 7 8 8.8 6 11.5z" fill="var(--gold)"/><circle cx="6" cy="4.9" r="1.3" fill="var(--card-white)"/></svg>
      <span>Your address line1<br>Your address line 2</span>
    </li>
  </ul>

  <p class="website">www.<span class="accent">yourweb</span>.com</p>
</section>

<section class="card card--back" aria-label="Business card back">
  <h2 class="company-name">
    <span class="word-main">Harbourline</span>
    <span class="word-sub">Holdings</span>
  </h2>
</section>

</body>
</html>
```